Harvest Gathering event flyer

I would like a church event flyer designed. The event is called "HARVEST GATHERING 2018". I am looking for a professional, yet catchy design that uses our brand colors and logo creatively while communicating key information of the event effectively.

1. The logo is attached in two color formats. The designer has the choice to use them as he/she want.

2. The location of the event is: Lindqvist Community Center, 482 Tamsworth Street, Portland, ME 04102
3. Time and date of event. The designer can organize and format the date and time as he/she pleases.
December 28th, 29th @ 7:00PM
December 30th @ 10:00AM
4. The topic of the event is "Tongues of fire". The designer is free to use this phrase as he/she pleases to create a good composition.
5. Speaker: Prophet Marcus Obuya
6. Contact information: contact@cedarbrookfellowship.org - Telephone number: 207 555 0148

7. I would also like the following three words on the flyer. These words describe the focus of the event: FIRE, REVIVAL, PROPHETIC

```html
<!DOCTYPE html>
<html lang="en">
<head>
<meta charset="utf-8">
<title>Harvest Gathering 2018 Flyer</title>
<link rel="stylesheet" href="https://fonts.googleapis.com/css2?family=Abril+Fatface&family=Old+Standard+TT:wght@400;700&family=Saira+Condensed:wght@300&display=swap">
<style>
  :root {
    --navy: #0a2a4a;
    --stage: #0b2946;
    --orange: #f39623;
    --white: #ffffff;
    --mist: #c9d6ee;
    --mist-deep: #a9bbe0;
  }
  * { box-sizing: border-box; margin: 0; padding: 0; }
  html, body {
    width: 1200px; height: 1200px; overflow: hidden;
    background: var(--stage);
  }
  .flyer {
    position: absolute; left: 220px; top: 60px;
    width: 760px; height: 1080px;
    background: var(--white);
    overflow: hidden;
    font-family: "Old Standard TT", Georgia, serif;
    color: var(--navy);
  }
  .crowd-backdrop {
    position: absolute; left: 0; right: 0; bottom: 0; height: 420px;
    background: linear-gradient(to bottom, rgba(255,255,255,0) 0%, var(--mist) 55%, var(--mist-deep) 100%);
  }
  .frame {
    position: absolute; left: 40px; top: 40px;
    width: 440px; height: 800px;
    border-left: 2px solid var(--navy);
    border-top: 2px solid var(--navy);
    border-top-left-radius: 34px;
  }
  .brand {
    position: absolute; left: 505px; top: 62px;
    display: flex; align-items: center; gap: 10px;
  }
  .brand-dot {
    width: 22px; height: 22px; border-radius: 50%;
    background: var(--orange);
  }
  .brand-name {
    font-family: "Old Standard TT", Georgia, serif;
    font-weight: 400; font-size: 46px; letter-spacing: 1px;
    color: var(--navy);
  }
  .title-main {
    position: absolute; left: 62px; top: 128px;
    font-family: "Abril Fatface", Georgia, serif;
    font-size: 112px; line-height: 1; letter-spacing: 2px;
    color: var(--orange);
  }
  .title-sub {
    position: absolute; left: 66px; top: 252px;
    font-family: "Abril Fatface", Georgia, serif;
    font-size: 54px; line-height: 1; letter-spacing: 2px;
    color: var(--navy);
  }
  .focus-words {
    position: absolute; left: 68px; top: 330px;
    font-size: 18px; font-weight: 700; letter-spacing: 4px;
    color: var(--orange);
  }
  .focus-words .sep { color: var(--navy); padding: 0 6px; }
  .topic {
    position: absolute; left: 92px; top: 395px;
    font-family: "Saira Condensed", "Arial Narrow", sans-serif;
    font-weight: 300; font-size: 88px; line-height: 0.95;
    color: var(--navy);
  }
  .topic .accent { color: var(--orange); }
  .topic .line2 { display: block; }
  .flame-art {
    position: absolute; left: 380px; top: 410px;
    width: 130px; height: 210px;
    border-radius: 60% 40% 50% 50% / 70% 60% 40% 40%;
    background: var(--orange);
  }
  .speaker {
    position: absolute; left: 330px; top: 650px;
    font-size: 17px;
  }
  .speaker strong { font-size: 21px; font-weight: 700; }
  .venue {
    position: absolute; left: 92px; top: 690px;
    font-size: 21px; font-weight: 700; line-height: 1.25;
  }
  .divider {
    position: absolute; left: 92px; top: 762px;
    width: 470px; height: 3px;
    background: linear-gradient(to right, var(--orange), rgba(243,150,35,0));
  }
  .schedule {
    position: absolute; left: 86px; top: 776px;
    font-weight: 700; line-height: 1.15;
  }
  .schedule .month { font-size: 20px; display: block; }
  .schedule .day { font-size: 30px; }
  .schedule .time { font-size: 17px; }
  .contact-band {
    position: absolute; left: 0; top: 870px;
    width: 640px; height: 150px;
    background: var(--orange);
    text-align: center; padding-top: 14px;
  }
  .contact-band .call { font-size: 20px; font-weight: 700; color: var(--navy); display: block; }
  .contact-band .phone {
    font-family: "Abril Fatface", Georgia, serif;
    font-size: 62px; line-height: 1.1; letter-spacing: 2px; color: var(--white); display: block;
  }
  .contact-band .email { font-size: 20px; color: var(--navy); display: block; }
</style>
</head>
<body>
  <main class="flyer">
    <div class="crowd-backdrop" role="img" aria-label="Faint photo of a worshipping crowd with raised hands, in soft pale blue tones"></div>
    <div class="frame"></div>

    <div class="brand">
      <span class="brand-dot"></span>
      <span class="brand-name">KAVELO</span>
    </div>

    <h1 class="title-main">HARVEST</h1>
    <h2 class="title-sub">GATHERING 2018</h2>

    <p class="focus-words">FIRE<span class="sep">•</span>REVIVAL<span class="sep">•</span>PROPHETIC</p>

    <p class="topic">Tongues<span class="line2">of <span class="accent">fire</span></span></p>
    <div class="flame-art" role="img" aria-label="Stylised orange flame illustration"></div>

    <p class="speaker">Speaker: <strong>Prophet Marcus Obuya</strong></p>

    <p class="venue">Lindqvist Community Center<br>482 Tamsworth Street, Portland, ME 04102</p>
    <div class="divider"></div>

    <p class="schedule">
      <span class="month">December</span>
      <span class="day">28th, 29th</span> <span class="time">@ 7:00PM</span>
      <span class="time">&nbsp;|&nbsp;</span>
      <span class="day">30th</span> <span class="time">@ 10:00AM</span>
    </p>

    <section class="contact-band">
      <span class="call">CALL</span>
      <span class="phone">207 555 0148</span>
      <span class="email">contact@cedarbrookfellowship.org</span>
    </section>
  </main>
</body>
</html>
```